Crestline Podiatry Needs a Branded 8.5 x 11 template

We need a single template that will reflect our brand and have a really interesting and catchy feel. Be creative. It should include our logo a catch phrase like "Where Your Feet Are in Good Hands" and editable. There should be a header with this information. The central portion should be available to place text about medical conditions or other information and available to take pictures.
The footer needs to be all of the info on our location such as address, phone, drs names etc. - see must haves
We like shadows, 3D, really creative and catchy.
Below is an example that my friend uses. I like it but would like something a little more interesting. I do not want the same design as the flyer attached.
Logo is attached.
Our Colors: Want plenty of white space
#FAC000
#9F38AA

Target Market(s)

Patients and Physicians. We are podiatrists, foot and ankle specialists but I do not want any pictures of feet or medical stuff on the template.

Industry/Entity Type

Medical

Requirements
Must have
• For the Footer: Make it creative please

Physicians and Surgeons of the Foot and Ankle
Dr. Owen Brellis
Dr. Harriet Vandermolen
Address 4187 N. Corliss Blvd. Suite 508, Tampa, FL 33614
phone - 813-462-0197
email office@crestlinepodiatrygroup.net
web http://www.theGulfsideFootClinic.net

The Tagline section in the header needs to be editable so I can make changes. The middle section also needs to be editable.

I prefer to make edits in Photoshop or possibly Illustrator

```html
<!DOCTYPE html>
<html lang="en">
<head>
<meta charset="utf-8">
<title>Crestline Podiatry Letterhead</title>
<link href="https://fonts.googleapis.com/css2?family=Source+Sans+3:wght@400;600&family=PT+Sans+Narrow:wght@400;700&display=swap" rel="stylesheet">
<style>
  :root {
    --backdrop: #e6e4e1;
    --paper: #ffffff;
    --purple: #9f38aa;
    --gold: #fac000;
    --ink: #1e1e1e;
    --ink-soft: #3a3a3a;
    --cream: #f3ead2;
  }
  html, body {
    margin: 0;
    padding: 0;
    width: 1040px;
    height: 1200px;
    overflow: hidden;
    background: var(--backdrop);
  }
  .letterhead {
    position: absolute;
    left: 70px;
    top: 18px;
    width: 900px;
    height: 1164px;
    background: var(--paper);
    box-shadow: 0 6px 24px rgba(0,0,0,0.25);
    overflow: hidden;
  }
  .letterhead-art {
    position: absolute;
    inset: 0;
    width: 900px;
    height: 1164px;
  }
  .brand-name {
    position: absolute;
    left: 0;
    width: 900px;
    top: 103px;
    margin: 0;
    text-align: center;
    font-family: "Source Sans 3", sans-serif;
    font-weight: 400;
    font-size: 36px;
    line-height: 40px;
    color: var(--ink);
  }
  .footer-card {
    position: absolute;
    right: 25px;
    top: 1057px;
    width: 470px;
    text-align: right;
    font-family: "PT Sans Narrow", sans-serif;
    color: var(--ink-soft);
    letter-spacing: -0.2px;
  }
  .footer-card p { margin: 0; white-space: nowrap; }
  .footer-tagline { font-size: 14px; line-height: 18px; font-weight: 700; color: var(--ink); }
  .footer-doctors { font-size: 15px; line-height: 19px; margin-top: 1px !important; }
  .footer-contact { font-size: 12px; line-height: 16px; }
  .footer-contact b { font-weight: 700; color: var(--ink); }
  .sep { padding: 0 5px; }
</style>
</head>
<body>
  <div class="letterhead">
    <svg class="letterhead-art" viewBox="0 0 833 1078" preserveAspectRatio="none" aria-hidden="true">
      <defs>
        <linearGradient id="band-shade" x1="0" x2="1" y1="0" y2="0">
          <stop offset="0" stop-color="#5e5e5e"/>
          <stop offset="0.05" stop-color="#dcdcdc"/>
          <stop offset="0.2" stop-color="#f7f7f7"/>
          <stop offset="0.8" stop-color="#f7f7f7"/>
          <stop offset="0.95" stop-color="#dcdcdc"/>
          <stop offset="1" stop-color="#5e5e5e"/>
        </linearGradient>
        <linearGradient id="band-gloss" x1="0" x2="0" y1="0" y2="1">
          <stop offset="0" stop-color="#ffffff" stop-opacity="0.6"/>
          <stop offset="0.7" stop-color="#ffffff" stop-opacity="0"/>
          <stop offset="1" stop-color="#bdbdbd" stop-opacity="0.5"/>
        </linearGradient>
        <linearGradient id="purple-fill" x1="0" x2="1" y1="0" y2="1">
          <stop offset="0" stop-color="#a468ad"/>
          <stop offset="0.5" stop-color="#9a55a6"/>
          <stop offset="1" stop-color="#8e3f9c"/>
        </linearGradient>
        <linearGradient id="gold-fill" x1="0" x2="1" y1="0" y2="0">
          <stop offset="0" stop-color="#e4b51a"/>
          <stop offset="1" stop-color="#f1bc10"/>
        </linearGradient>
        <linearGradient id="panel-fill" x1="0" x2="0" y1="0" y2="1">
          <stop offset="0" stop-color="#e6e6e6"/>
          <stop offset="0.38" stop-color="#fbfbfb"/>
          <stop offset="0.6" stop-color="#ffffff"/>
          <stop offset="1" stop-color="#e2e2e2"/>
        </linearGradient>
        <linearGradient id="silver-sweep" x1="0" x2="1" y1="0" y2="0">
          <stop offset="0" stop-color="#d6d6d6"/>
          <stop offset="0.7" stop-color="#ffffff"/>
          <stop offset="1" stop-color="#cfcfcf"/>
        </linearGradient>
        <linearGradient id="card-fill" x1="0" x2="1" y1="0" y2="0">
          <stop offset="0" stop-color="#f7f1df"/>
          <stop offset="1" stop-color="#efe3c2"/>
        </linearGradient>
        <filter id="soft-shadow" x="-10%" y="-10%" width="120%" height="130%">
          <feDropShadow dx="0" dy="4" stdDeviation="5" flood-color="#000" flood-opacity="0.35"/>
        </filter>
      </defs>

      <!-- purple sweep behind the writing panel -->
      <path d="M0 400 Q 300 290 833 242 L833 1078 L0 1078 Z" fill="#ffffff"/>
      <path d="M0 440 Q 320 310 833 262 L833 1078 L0 1078 Z" fill="url(#purple-fill)"/>

      <!-- header band -->
      <rect x="34" y="42" width="766" height="128" fill="url(#band-shade)" filter="url(#soft-shadow)"/>
      <rect x="34" y="42" width="766" height="128" fill="url(#band-gloss)"/>

      <!-- writing panel -->
      <rect x="55" y="178" width="723" height="834" fill="#ffffff" filter="url(#soft-shadow)"/>
      <rect x="69" y="190" width="695" height="812" fill="url(#panel-fill)"/>

      <!-- lower silver and gold sweeps -->
      <path d="M0 1005 Q 520 1000 833 830 L833 1078 L0 1078 Z" fill="url(#silver-sweep)"/>
      <path d="M0 1030 Q 520 1020 833 868 L833 1078 L0 1078 Z" fill="url(#gold-fill)"/>

      <!-- footer card -->
      <rect x="388" y="972" width="445" height="106" fill="url(#card-fill)" filter="url(#soft-shadow)"/>
      <rect x="390" y="974" width="441" height="102" fill="none" stroke="#ffffff" stroke-opacity="0.7"/>
    </svg>

    <h1 class="brand-name">Crestline Podiatry</h1>

    <footer class="footer-card">
      <p class="footer-tagline">Physicians and Surgeons of the Foot and Ankle</p>
      <p class="footer-doctors">Dr. Owen Brellis <span class="sep">|</span> Dr. Harriet Vandermolen</p>
      <p class="footer-contact"><b>Address:</b> 4187 N. Corliss Blvd. Suite 508, Tampa, FL 33614 <span class="sep">|</span> <b>Phone:</b> 813-462-0197</p>
      <p class="footer-contact"><b>Email:</b> office@crestlinepodiatrygroup.net <span class="sep">|</span> <b>Web:</b> http://www.theGulfsideFootClinic.net</p>
    </footer>
  </div>
</body>
</html>
```